Vr holdings enterprise pty ltd

2 sided card black and red with white
Very professional and elegant

Target Market(s)

Construction and Development

Industry/Entity Type

Construction and development

Contact Information for Business Card

One side black, one side red/or white business logo in top corner, email: morgan@vrholdingsgroup.example

Requirements
Should not have
• Blue

```html
<!DOCTYPE html>
<html lang="en">
<head>
<meta charset="utf-8">
<title>VR Holdings – Business Card</title>
<link href="https://fonts.googleapis.com/css2?family=Open+Sans:ital,wght@0,400;0,700;1,400&display=swap" rel="stylesheet">
<style>
  :root {
    --stage: #141414;
    --card: #2a2a2a;
    --card-edge: #333333;
    --red: #e8402a;
    --white: #ffffff;
    --muted: #e6e6e6;
    --pattern-dark: #1e1e1e;
    --pattern-light: #4a4a4a;
  }
  * { margin: 0; padding: 0; box-sizing: border-box; }
  html, body {
    width: 1200px;
    height: 900px;
    overflow: hidden;
    background: var(--stage);
    font-family: "Open Sans", Arial, sans-serif;
  }
  .stage {
    width: 1200px;
    height: 900px;
    display: flex;
    flex-direction: column;
    align-items: center;
    justify-content: center;
    gap: 40px;
  }
  .card {
    width: 700px;
    height: 400px;
    border-radius: 22px;
    background: var(--card);
    position: relative;
    overflow: hidden;
    box-shadow: 0 10px 30px rgba(0,0,0,0.5);
  }

  /* Front */
  .card-front .contact {
    position: absolute;
    left: 60px;
    top: 110px;
  }
  .contact-name {
    color: var(--red);
    font-weight: 700;
    font-size: 30px;
    letter-spacing: 0.5px;
    text-transform: uppercase;
    line-height: 1.1;
  }
  .contact-title {
    color: var(--muted);
    font-size: 18px;
    margin-top: 2px;
    margin-bottom: 22px;
  }
  .contact-list { list-style: none; }
  .contact-item {
    display: flex;
    align-items: center;
    gap: 12px;
    color: var(--muted);
    font-size: 17px;
    line-height: 1.75;
  }
  .contact-icon { width: 16px; height: 16px; flex: none; }

  .brand {
    position: absolute;
    right: 60px;
    top: 150px;
    display: flex;
    align-items: center;
    gap: 12px;
  }
  .brand-name {
    color: var(--white);
    font-weight: 700;
    font-size: 38px;
    letter-spacing: 1px;
    text-transform: uppercase;
  }
  .brand-dot {
    width: 12px;
    height: 12px;
    border-radius: 50%;
    background: var(--red);
    align-self: flex-end;
    margin-bottom: 10px;
  }

  /* Back */
  .card-back .pattern {
    position: absolute;
    inset: 0;
    background: linear-gradient(135deg, var(--pattern-dark) 0%, var(--pattern-dark) 45%, var(--pattern-light) 100%);
  }
  .card-back .brand-small {
    position: absolute;
    left: 40px;
    bottom: 30px;
    color: var(--red);
    font-weight: 700;
    font-size: 20px;
    letter-spacing: 1px;
    text-transform: uppercase;
  }
</style>
</head>
<body>
<main class="stage">

  <section class="card card-front" aria-label="Business card front">
    <div class="contact">
      <h1 class="contact-name">Jordan Hale</h1>
      <p class="contact-title">Managing Director</p>
      <ul class="contact-list">
        <li class="contact-item">
          <svg class="contact-icon" viewBox="0 0 16 16" aria-hidden="true">
            <path d="M3 1.5h3l1.2 3.2-1.8 1.2a9 9 0 0 0 4.7 4.7l1.2-1.8 3.2 1.2v3a1.5 1.5 0 0 1-1.6 1.5A13 13 0 0 1 1.5 3.1 1.5 1.5 0 0 1 3 1.5z" fill="var(--red)"/>
          </svg>
          +000 555 0142
        </li>
        <li class="contact-item">
          <svg class="contact-icon" viewBox="0 0 16 16" aria-hidden="true">
            <rect x="1" y="3" width="14" height="10" rx="1" fill="var(--red)"/>
            <path d="M1.5 3.8 8 9l6.5-5.2" fill="none" stroke="var(--card)" stroke-width="1.3"/>
          </svg>
          morgan@vrholdingsgroup.example
        </li>
        <li class="contact-item">
          <svg class="contact-icon" viewBox="0 0 16 16" aria-hidden="true">
            <circle cx="8" cy="8" r="7" fill="var(--red)"/>
            <path d="M1 8h14M8 1c-2.5 2-2.5 12 0 14M8 1c2.5 2 2.5 12 0 14" fill="none" stroke="var(--card)" stroke-width="1"/>
          </svg>
          www.vrholdingsgroup.example
        </li>
      </ul>
    </div>
    <div class="brand">
      <span class="brand-name">VR Holdings</span>
      <span class="brand-dot" aria-hidden="true"></span>
    </div>
  </section>

  <section class="card card-back" aria-label="Business card back">
    <div class="pattern" role="img" aria-label="Repeating monogram pattern in tonal greys across the card back"></div>
    <span class="brand-small">VR Holdings</span>
  </section>

</main>
</body>
</html>
```